Construction Website Design for Wordpress

Update:
I like this theme as a starting point. It seems like a very good start. Fonts, colors, motion, etc. https://consultancy.qrvistaweb.com/
***************************************************************************************

I want a new website design that can be implemented in wordpress. Here is my existing site: www.halvornquantax.com
Attached is a document with the copy, requirements, sample images, etc. Let me know what questions you have.

Here is a sample of the info, but review the attached document for everything:

Website layout:
Title Bar
• Home
• Expertise
• Takeoffs
• Divisions Serviced (redesign from orig page: (http://www.halvornquantax.com/scope-list/)
• Member Login
Requirements
• Home page has a slider with 3 dimmed commercial construction images and copy overlay
• Request for Proposal Form should be over the slider and the same look and location on every page.
• “Request For Proposal” – No Obligation
o Company Name
o Contact Name
o Contact Phone
o Contact Email
• Use the copy below for the pages
• Split the Client Testimonials among the pages

Target Market(s)

B2B - Construction Companies

Industry/Entity Type

Construction

Number of Pages Required

4 page

Font styles to use
Serif

Colors
0255a3
3276b5
85abd2
d0dfed

Requirements
Must have
• Construction images in slider
• Request for proposal form
• testimonials

```html
<!DOCTYPE html>
<html lang="en">
<head>
<meta charset="utf-8">
<title>Halvorn Quantax – Construction Takeoff Experts</title>
<link rel="stylesheet" href="https://fonts.googleapis.com/css2?family=Open+Sans:wght@400;600;700;800&display=swap">
<style>
:root{
  --navy:#164a7c;
  --navy-dark:#123f6c;
  --heading:#154d80;
  --accent:#1a86d0;
  --sky:#def2fc;
  --text:#4a4a4a;
  --rule:#b9b9b9;
  --white:#ffffff;
}
*{box-sizing:border-box;margin:0;padding:0}
html,body{width:833px;height:1200px;overflow:hidden}
body{position:relative;font-family:"Open Sans",Arial,sans-serif;background:var(--white);color:var(--text)}
.abs{position:absolute}

/* header */
.site-header{position:absolute;left:0;top:0;width:833px;height:68px;background:var(--white)}
.brand{position:absolute;left:120px;top:14px;display:flex;align-items:center;gap:7px}
.brand-mark{width:12px;height:12px;border-radius:50%;background:var(--accent)}
.brand-name{font-size:17px;font-weight:700;color:var(--navy);letter-spacing:.3px;line-height:1}
.brand-tag{position:absolute;left:139px;top:34px;font-size:8.5px;font-weight:600;color:var(--accent);letter-spacing:.2px}
.login-btn{position:absolute;left:619px;top:10px;width:93px;height:26px;background:var(--navy);color:var(--white);font-size:8.5px;display:flex;align-items:center;justify-content:center;gap:5px}
.main-nav{position:absolute;top:45px;right:120px;display:flex;gap:24px;font-size:10px;color:#333}
.main-nav .current{color:var(--navy)}

/* hero */
.hero{position:absolute;left:0;top:68px;width:833px;height:312px;background:linear-gradient(180deg,#8fb0d8 0%,#a9c4e4 45%,#c9d8ea 100%)}
.hero-photo{position:absolute;left:0;top:0;width:833px;height:312px;background:linear-gradient(100deg,#5b5048 0%,#7b6d60 25%,#a9b6c9 55%,rgba(169,196,228,0) 75%)}
.slide-arrow{position:absolute;top:144px;width:26px;height:26px}
.hero-title{position:absolute;right:121px;top:86px;font-size:27px;font-weight:800;color:var(--navy);letter-spacing:.5px;line-height:1}
.hero-sub{position:absolute;right:121px;top:120px;font-size:14px;line-height:19px;color:#222;text-align:right}

/* proposal form */
.rfp{position:absolute;left:491px;top:171px;width:222px;height:228px;background:var(--accent);padding:12px 11px}
.rfp h2{font-size:15px;font-weight:700;color:var(--white);text-align:center;letter-spacing:.3px;line-height:18px;margin-bottom:11px}
.rfp .field{height:29px;background:var(--white);font-size:8.5px;color:#333;padding-left:12px;display:flex;align-items:center;margin-bottom:7.5px}
.rfp .submit{height:28px;margin-top:1px;background:var(--navy);color:var(--white);font-size:10px;font-weight:700;display:flex;align-items:center;justify-content:center;letter-spacing:.3px}

/* about */
.about-photo{position:absolute;left:120px;top:452px;width:222px;height:326px;background:linear-gradient(180deg,#a6b6c6 0%,#6f7369 45%,#4d4a3d 70%,#8a8a3e 100%)}
.about{position:absolute;left:363px;top:448px;width:350px}
.about h1{font-size:21px;font-weight:700;color:var(--heading);line-height:26px;margin-bottom:8px}
.about h3{font-size:13px;font-weight:700;color:var(--accent);line-height:16px;margin-bottom:4px}
.about p{font-size:8.2px;line-height:13.6px;color:var(--text);margin-bottom:6px}
.about hr{border:0;border-top:1px solid var(--rule);margin:14px 0 15px}

/* testimonials */
.clients{position:absolute;left:0;top:831px;width:833px;height:297px;background:var(--sky)}
.clients h2{position:absolute;left:0;top:47px;width:833px;text-align:center;font-size:21px;font-weight:700;color:var(--heading)}
.quote{position:absolute;top:88px;width:276px;height:83px;background:var(--white);padding:15px 16px;font-size:7.6px;line-height:13.6px;color:#333}
.quote::after{content:"";position:absolute;left:0;bottom:-16px;border-left:0 solid transparent;border-right:18px solid transparent;border-top:16px solid var(--white);margin-left:1px}
.client{position:absolute;top:193px;display:flex;align-items:center;gap:13px}
.avatar{width:52px;height:52px;border-radius:50%;background:linear-gradient(180deg,#b9a895,#8d7a66)}
.client-name{font-size:10.5px;color:var(--navy);line-height:14px}
.client-co{font-size:7.5px;color:#666;line-height:12px}
.chev{position:absolute;top:124px}

/* footer */
.site-footer{position:absolute;left:0;top:1128px;width:833px;height:72px;background:var(--navy)}
.foot-nav{position:absolute;left:120px;top:20px;font-size:7.8px;color:#d6e4f2}
.foot-nav span{margin:0 6px}
.copy{position:absolute;left:120px;top:41px;font-size:7.8px;color:#b9cde2}
.social{position:absolute;top:31px;width:10px;height:10px;border-radius:50%;background:#b9cde2}
</style>
</head>
<body>

<header class="site-header">
  <div class="brand"><span class="brand-mark"></span><span class="brand-name">HALVORN QUANTAX</span></div>
  <div class="brand-tag">CONSTRUCTION TAKEOFF EXPERTS</div>
  <div class="login-btn">
    <svg width="9" height="9" viewBox="0 0 10 10"><path d="M1 5h5M4 2.5 6.5 5 4 7.5" stroke="#fff" stroke-width="1.6" fill="none"/><path d="M6 1h3v8H6" stroke="#fff" stroke-width="1.4" fill="none"/></svg>
    MEMBER LOGIN
  </div>
  <nav class="main-nav"><span class="current">Home</span><span>Expertise</span><span>Takeoffs</span><span>Divisions Serviced</span></nav>
</header>

<section class="hero">
  <div class="hero-photo" role="img" aria-label="Ironworkers in hard hats seated on a steel beam against a blue sky"></div>
  <svg class="slide-arrow" style="left:35px" viewBox="0 0 26 26"><circle cx="13" cy="13" r="12" fill="#1a86d0" stroke="#fff" stroke-width="2"/><path d="M15 7.5 9.5 13l5.5 5.5" stroke="#fff" stroke-width="2.6" fill="none"/></svg>
  <svg class="slide-arrow" style="left:771px" viewBox="0 0 26 26"><circle cx="13" cy="13" r="12" fill="#1a86d0" stroke="#fff" stroke-width="2"/><path d="M11 7.5 16.5 13 11 18.5" stroke="#fff" stroke-width="2.6" fill="none"/></svg>
</section>
<div class="hero-title">CONFIDENCE</div>
<div class="hero-sub">Accurate and reliable, we help you<br>propose on more work without risk</div>

<form class="rfp">
  <h2>REQUEST FOR PROPOSAL</h2>
  <div class="field">Company Name</div>
  <div class="field">Contact Name</div>
  <div class="field">Contact Phone</div>
  <div class="field">Contact Email</div>
  <div class="submit">SUBMIT</div>
</form>

<div class="about-photo" role="img" aria-label="Safety officer in a high-visibility vest looking up at scaffolding"></div>
<section class="about">
  <h1>HALVORN QUANTAX</h1>
  <p>Dedicated to saving our clients time and money by specializing in accurate, reliable materials quantity calculations, Halvorn Quantax allows general contractors to confidently propose on more work with less stress.</p>
  <p>To receive a no-obligation answer to your takeoff needs complete the Request for Proposal form. Halvorn Quantax will provide a comprehensive proposal detailing the hours required and payment options that are easily refined to both near- and long-term needs.</p>
  <hr>
  <h3>PROCESS</h3>
  <p>Once the proposal is approved, clients fund their account and allocate their hours as desired - project-by-project, monthly, as-needed, or otherwise. Our service and products are completely tailored to each client based on the fundamental factors that make your business distinct from all others.</p>
  <hr>
  <h3>BENEFITS</h3>
  <p>Accurate, reliable quantities delivered as-scheduled and expected allow your key staff to invest their time in quality, safety, profit, and client relationships. An extra set of hands in your bid room helps you put out more proposals and takes a tedious task off your to-do list whenever you need it without the obligation of a full-time salary.</p>
</section>

<section class="clients">
  <h2>WHAT CLIENTS SAY</h2>
  <svg class="chev" style="left:61px" width="10" height="16" viewBox="0 0 10 16"><path d="M8 2 2 8l6 6" stroke="#9aa3ab" stroke-width="2" fill="none"/></svg>
  <svg class="chev" style="left:761px" width="10" height="16" viewBox="0 0 10 16"><path d="M2 2l6 6-6 6" stroke="#9aa3ab" stroke-width="2" fill="none"/></svg>

  <div class="quote" style="left:120px">“ Halvorn Quantax does outstanding work, accurate, detailed, and reliable. The consultant on my account knows what I want in the break-down and produces the information exactly as I need it. Time, money and confidence, Halvorn Quantax hits the mark every time.. ”</div>
  <div class="client" style="left:120px">
    <div class="avatar" role="img" aria-label="Client portrait"></div>
    <div><div class="client-name">Dana Morrow, President</div><div class="client-co">Ridgeline Roofing</div></div>
  </div>

  <div class="quote" style="left:437px">“ We get an influx of great opportunities and sometimes it’s more than we can handle. Halvorn Quantax fills the gap and helped us to grow our business. It’s really excellent to have a genuine, always-ready ally in our estimating efforts. ”</div>
  <div class="client" style="left:437px">
    <div class="avatar" role="img" aria-label="Client portrait"></div>
    <div><div class="client-name">Priya Velandi</div><div class="client-co">Eastbay Builders, LLC.</div></div>
  </div>
</section>

<footer class="site-footer">
  <div class="foot-nav">Home<span>|</span>Expertise<span>|</span>Takeoffs<span>|</span>Divisions Serviced</div>
  <div class="copy">Copyright © 2019 Halvorn Quantax, All rights reserved.</div>
  <span class="social" style="left:679px" aria-label="Social link"></span>
  <span class="social" style="left:701px" aria-label="Social link"></span>
</footer>

</body>
</html>
```